Holiday Rental Company Flyer Design (DL not A5)

Note from PixelFolk Administration: The category sizing selected is A5, however the project requires DL sized artwork. Please refer to the DL template link below while the 'Special Requirements' are updated accordingly.

Project Brief:
We need a double sided DL flyer designed for an up market Holiday Rental Company that portrays a personalised approach to property management. These are to be used for letter box drops to homes we're specifically targeting so the design should be modern, complimentary colour palette, uncluttered & visually appealing.

Please Download the DL Template from Quillmark here: http://www.quillmark.com.au/qm/ns/propath/UploadResources.aspx?selectedTab=0?pfid=BFB&pf_id=BFB&xnav=easypath-upload-image#Templates

Target Market(s)

Wealthy Home Owners

Industry/Entity Type

It Company

Font styles to use
Other font styles liked:
• Avant Garde Extra Light & Demi

Colors
33b8a4

Requirements
Must have
• DL Flyer sizes (210mm width x 99mm width, plus 3mm bleed)
• Front: Logo, Main Image & Grab
• Back: Contact Details & Brief Description of our business
• Images: Ideally the main image should be the house with the pool but alternatively a lifestyle images could also be used.
Nice to have
• A creative designer!
Should not have
• Clutter & busy designs

```html
<!DOCTYPE html>
<html lang="en">
<head>
<meta charset="utf-8">
<title>Harbourline Stays – Meet &amp; Greet Flyer</title>
<link href="https://fonts.googleapis.com/css2?family=Questrial&family=Poppins:wght@500;600&display=swap" rel="stylesheet">
<style>
  :root {
    --mint: #4ff28f;
    --mint-soft: rgba(79, 242, 143, 0.35);
    --slate: #3d4447;
    --ink: #333a3d;
    --paper: #ffffff;
    --backdrop: #ececec;
    --teal-deep: #2f8f86;
  }
  * { box-sizing: border-box; margin: 0; padding: 0; }
  html, body { width: 733px; height: 1200px; overflow: hidden; }
  body { background: var(--backdrop); font-family: "Questrial", sans-serif; color: var(--ink); position: relative; }

  .flyer { position: absolute; left: 103px; top: 55px; width: 527px; height: 1097px; background: var(--paper); overflow: hidden; box-shadow: 0 4px 14px rgba(0,0,0,0.18); }

  .photo-column { position: absolute; left: 0; top: 0; width: 260px; height: 808px; }
  .photo { position: absolute; left: 0; width: 260px; }
  .photo--lounge { top: 0; height: 401px; background: linear-gradient(180deg, #7fc9c9 0%, #5fb7ab 30%, #8fd6b9 60%, #b9e6cf 100%); }
  .photo--bathroom { top: 401px; height: 200px; background: linear-gradient(160deg, #bfe9d6 0%, #95d8b8 55%, #a7e2c4 100%); }
  .photo--bedroom { top: 601px; height: 207px; background: linear-gradient(150deg, #cfe9c9 0%, #8fe68a 45%, #e2a06a 80%, #d36a4f 100%); }
  .photo-tint { position: absolute; left: 27px; top: 0; width: 233px; height: 808px; background: var(--mint-soft); mix-blend-mode: screen; }

  .intro { position: absolute; left: 38px; top: 48px; width: 196px; color: var(--paper); }
  .intro__title { font-family: "Poppins", sans-serif; font-weight: 600; font-size: 26px; line-height: 1.2; text-align: center; }
  .intro__text { margin-top: 22px; font-size: 15px; line-height: 1.22; text-align: justify; }

  .brand { position: absolute; left: 260px; top: 108px; width: 267px; text-align: center; color: var(--mint); }
  .brand__name { font-size: 22px; letter-spacing: 3px; line-height: 1.15; text-transform: uppercase; }
  .brand__dot { display: block; margin: 10px auto 0; width: 26px; height: 26px; border: 1.5px solid var(--mint); border-radius: 50%; }

  .service { position: absolute; left: 292px; top: 220px; width: 200px; font-size: 16.5px; line-height: 1.2; }
  .service strong { font-family: "Poppins", sans-serif; font-weight: 600; color: var(--mint); }

  .step-badge { position: absolute; left: 229px; width: 70px; height: 70px; border-radius: 50%; background: var(--paper); box-shadow: 0 2px 6px rgba(0,0,0,0.25); }
  .step-badge span { position: absolute; left: 8px; top: 8px; width: 54px; height: 54px; border-radius: 50%; background: var(--mint); font-family: "Poppins", sans-serif; font-weight: 600; font-size: 26px; line-height: 54px; text-align: center; color: var(--ink); }
  .step-badge--one { top: 300px; }
  .step-badge--two { top: 455px; }
  .step-badge--three { top: 606px; }

  .step-text { position: absolute; left: 290px; width: 205px; font-size: 16px; line-height: 1.22; }
  .step-text--one { top: 380px; }
  .step-text--two { top: 545px; }
  .step-text--three { top: 693px; }

  .enquiry { position: absolute; left: 0; top: 808px; width: 527px; height: 159px; background: var(--slate); color: var(--paper); display: flex; align-items: center; justify-content: center; text-align: center; font-size: 21px; line-height: 1.3; padding: 0 30px; }
  .enquiry strong { font-family: "Poppins", sans-serif; font-weight: 600; color: var(--mint); }

  .contacts { position: absolute; left: 0; top: 967px; width: 527px; height: 130px; background: var(--mint); }
  .contact { position: absolute; display: flex; align-items: center; gap: 8px; font-size: 14px; color: var(--ink); }
  .contact svg { width: 22px; height: 22px; flex: none; }
  .contact--phone { left: 34px; top: 31px; }
  .contact--web { left: 34px; top: 66px; }
  .contact--email { left: 247px; top: 31px; }
  .contact--post { left: 247px; top: 66px; }
</style>
</head>
<body>
<main class="flyer">
  <div class="photo-column">
    <div class="photo photo--lounge" role="img" aria-label="Photo of a bright living room with glass vases overlooking the sea"></div>
    <div class="photo photo--bathroom" role="img" aria-label="Photo of a modern bathroom basin with flowers"></div>
    <div class="photo photo--bedroom" role="img" aria-label="Photo of a bed with green cushions and a colourful throw"></div>
    <div class="photo-tint"></div>
  </div>

  <section class="intro">
    <h1 class="intro__title">What we do differently!</h1>
    <p class="intro__text">Rather than relying upon a key safe or a central pick-up destination, a ‘Harbourline Stays’ staff member will greet guests upon arrival.</p>
  </section>

  <div class="brand">
    <div class="brand__name">Harbourline<br>Stays</div>
    <span class="brand__dot"></span>
  </div>

  <p class="service">Our <strong>‘Meet &amp; Greet’</strong> service provides home owners with an increased level of Security and also allows us to:</p>

  <div class="step-badge step-badge--one"><span>1</span></div>
  <p class="step-text step-text--one">Prepare the home for their arrival (lights, heaters, music etc.)</p>

  <div class="step-badge step-badge--two"><span>2</span></div>
  <p class="step-text step-text--two">Establish a rapport &amp; help facilitate future bookings</p>

  <div class="step-badge step-badge--three"><span>3</span></div>
  <p class="step-text step-text--three">Reiterate their responsibilities to ensure the return of their bond</p>

  <section class="enquiry">
    <p>If you’d like to know what your property could achieve or require additional information, <strong>please contact us on:</strong></p>
  </section>

  <section class="contacts">
    <div class="contact contact--phone">
      <svg viewBox="0 0 22 22" aria-hidden="true"><circle cx="11" cy="11" r="11" fill="#3d4447"/><path d="M7.5 6c.6-.4 1.2-.3 1.5.2l1 1.6c.3.5.1 1-.3 1.3l-.5.4c.5 1.2 1.4 2.1 2.6 2.7l.4-.5c.3-.4.9-.5 1.3-.2l1.6 1c.5.3.6 1 .2 1.5-.8 1-2 1.2-3.3.6-2-1-3.6-2.6-4.6-4.6C6.8 8 6.9 6.7 7.5 6z" fill="#fff"/></svg>
      <span>(03)5900 1234</span>
    </div>
    <div class="contact contact--web">
      <svg viewBox="0 0 22 22" aria-hidden="true"><circle cx="11" cy="11" r="11" fill="#3d4447"/><g fill="none" stroke="#fff" stroke-width="1.1"><circle cx="11" cy="11" r="5.5"/><ellipse cx="11" cy="11" rx="2.4" ry="5.5"/><path d="M5.5 11h11M6.3 8h9.4M6.3 14h9.4"/></g></svg>
      <span>harbourlinestays.com.au</span>
    </div>
    <div class="contact contact--email">
      <svg viewBox="0 0 22 22" aria-hidden="true"><circle cx="11" cy="11" r="11" fill="#3d4447"/><g fill="none" stroke="#fff" stroke-width="1.1"><rect x="5.5" y="7.5" width="11" height="7.5"/><path d="M5.5 7.5l5.5 4.3 5.5-4.3"/></g></svg>
      <span>stay@harbourlinestays.com.au</span>
    </div>
    <div class="contact contact--post">
      <svg viewBox="0 0 22 22" aria-hidden="true"><circle cx="11" cy="11" r="11" fill="#3d4447"/><rect x="5.5" y="8" width="11" height="6" rx="1.5" fill="#fff"/><rect x="7.5" y="10" width="4" height="1.4" fill="#3d4447"/><rect x="10.3" y="14" width="1.4" height="3" fill="#fff"/></svg>
      <span>PO Box 12, Seaview Victoria 3900</span>
    </div>
  </section>
</main>
</body>
</html>
```